Thabeni Academy one-page profile

I need to develop a professionally designed "one-pager" for a new independent school opening in the Mavuso Township in South Africa in 2015. Mavuso is one of the poorest communities in South Africa and our aim is to bring a university preparatory education to this community. The school will open with kindergarten students and will expand each year until we reach grade 12. I would like for the file to be in a format that I can easily edit in the event that the information that I provide in the attachment changes or should I choose to utilize the format for an additional flyer.

The document needs to be designed as an A4 paper sized document as opposed to the standard size used in the United States.

I like the format of the following document:
http://www.brelvonschools.org/pdfs/11.30.2012%20BNQS%20Tutoring%20One%20Pager.pdf
http://www.prindlework.com/images/150_Teacher_recruitment_flyer.jpg
http://slatehouse.org/2013/01/18/BRON%2520TQGS%2520Lottery%2520Information_English%2520Flyer%5B1%5D.jpg
Updates

I edited the attached Thabeni Academy one page profile by altering it slightly and cutting out some unnecessary wording.  Please view to make changes.

Target Market(s)

The target market for this piece are potential funders and partners.

Industry/Entity Type

University

Requirements
Must have
• The design must use the Thabeni Academy colors and fonts as outlined in the branding guide. The design must look professional and must give the impression of a stellar private school.
Should not have
• Clip art

```html
<!DOCTYPE html>
<html lang="en">
<head>
<meta charset="utf-8">
<title>Thabeni Academy – One-Page Profile</title>
<link rel="stylesheet" href="https://fonts.googleapis.com/css2?family=EB+Garamond:wght@400;500;600&family=Open+Sans:wght@600;700&display=swap">
<style>
  :root {
    --backdrop: #000000;
    --paper: #ffffff;
    --brand-blue: #2f6db3;
    --url-blue: #2d5a9a;
    --accent-orange: #f7941d;
    --panel-green: #8dc63f;
    --tile-orange: #f7941d;
    --tile-blue: #1f78c1;
    --tile-magenta: #a6137a;
    --tile-green: #8cc63e;
    --ink: #2a2a2a;
    --ink-light: #ffffff;
    --serif: "EB Garamond", Garamond, Georgia, serif;
    --sans: "Open Sans", Arial, sans-serif;
  }
  * { box-sizing: border-box; margin: 0; padding: 0; }
  html, body { width: 917px; height: 1200px; overflow: hidden; background: var(--backdrop); }
  .page {
    position: absolute; left: 87px; top: 75px; width: 742px; height: 1049px;
    background: var(--paper); font-family: var(--serif); color: var(--ink);
    font-size: 12px; line-height: 1.18;
  }
  .masthead { position: absolute; left: 0; top: 0; width: 100%; height: 134px; }
  .brand { position: absolute; left: 38px; top: 50px; display: flex; align-items: center; gap: 12px; }
  .brand-dot { width: 40px; height: 40px; border-radius: 50%; background: var(--brand-blue); }
  .brand-name { font-family: var(--serif); font-weight: 500; font-size: 24px; line-height: 1; color: var(--brand-blue); letter-spacing: 1px; }
  .site-url { position: absolute; right: 32px; top: 92px; font-size: 26px; color: var(--url-blue); }
  .hero-photo {
    position: absolute; left: 0; top: 134px; width: 100%; height: 311px;
    background: linear-gradient(120deg, #b43a2a 0%, #d9c25a 30%, #e7e2cf 55%, #6f8e9c 80%, #3a4f75 100%);
  }
  .orange-rule { position: absolute; left: 0; top: 445px; width: 274px; height: 17px; background: var(--accent-orange); }
  .side-column {
    position: absolute; left: 0; top: 462px; width: 274px; height: 587px;
    background: var(--brand-blue); color: var(--ink-light); padding: 17px 25px 0 25px;
  }
  .section-title { font-family: var(--serif); font-weight: 400; font-size: 15.5px; text-transform: uppercase; letter-spacing: 0.3px; margin-bottom: 1px; line-height: 1.1; }
  .side-column p { margin-bottom: 9px; }
  .side-column .section-title { margin-top: 6px; }
  .model-panel {
    position: absolute; left: 274px; top: 445px; width: 468px; height: 280px;
    background: var(--panel-green); color: var(--ink-light); padding: 13px 20px 0 15px;
  }
  .model-panel p { margin-bottom: 10px; }
  .feature-list { display: grid; grid-template-columns: 1fr 1fr; column-gap: 20px; list-style: none; margin-top: 4px; }
  .feature-list li { position: relative; padding-left: 20px; margin-bottom: 4px; }
  .feature-list li::before { content: ""; position: absolute; left: 5px; top: 5px; width: 5px; height: 5px; border-radius: 50%; background: var(--ink-light); }
  .core { position: absolute; left: 289px; top: 738px; width: 440px; }
  .core .section-title { color: var(--ink); font-size: 16px; }
  .core-intro { position: absolute; left: 0; top: 28px; width: 130px; }
  .tiles { position: absolute; left: 139px; top: 25px; display: grid; grid-template-columns: 144px 139px; grid-auto-rows: 83px; gap: 10px 5px; }
  .tile { color: var(--ink-light); display: flex; flex-direction: column; align-items: center; font-family: var(--sans); font-weight: 700; font-size: 10px; text-align: center; line-height: 1.1; padding-top: 2px; }
  .tile svg { margin-top: auto; margin-bottom: 8px; }
  .tile--justice { background: var(--tile-orange); }
  .tile--planning { background: var(--tile-blue); }
  .tile--literacy { background: var(--tile-magenta); }
  .tile--data { background: var(--tile-green); }
  .questions { position: absolute; left: 289px; top: 967px; width: 440px; }
  .questions .section-title { color: var(--ink); font-size: 16px; }
  .questions strong { font-weight: 600; font-size: 13.5px; }
</style>
</head>
<body>
<main class="page">
  <header class="masthead">
    <div class="brand"><span class="brand-dot"></span><span class="brand-name">THABENI ACADEMY</span></div>
    <div class="site-url">www.sizwefoundation.org</div>
  </header>

  <div class="hero-photo" role="img" aria-label="Photograph of a young child reading a picture book at a classroom table with colourful chairs behind"></div>
  <div class="orange-rule"></div>

  <aside class="side-column">
    <h2 class="section-title">Who Are We</h2>
    <p>Thabeni Academy will open its doors in January 2015 as the first Grade R- 12 university preparatory school in Mavuso. Admission to Thabeni Academy ison a first come, first serve basis and the schoolwill serve Grade R students in 2015 and will add a new grade each year.</p>
    <p>Thabeni Academy is a proud member of The Open Horizon Network of Schools, an organization, founded in the United States, committed to building a global network of transformational breakthrough schools.</p>
    <h2 class="section-title">Our Community</h2>
    <p>Mavusois a historic area located in the Gauteng Province in South Africa with several notable leaders residing in Mavuso at some point in their journey, including President Themba Ndlovu and former First Lady Lindiwe Khoza. Mavuso is a community full of promise but is considered one of the most economically disenfranchised urban communities in the country. The average household income in Mavuso is under R5000.00 per month and an estimated population of 500,000 people live on 1 square mile of land.</p>
    <h2 class="section-title">Our School Leader</h2>
    <p>Naledi Okafor-Dlamini is passionate about education and social justice and has been a contributing writer for Learning Review Africa and Classroom Forward and in 2012 Naledi gave a IdeasLive talk on the importance of an education steeped in social justice. Naledi is excited about the opportunity to learn and serve the Mavuso Township and is one of the organizers for IdeasLiveMavuso. In 2013,</p>
  </aside>

  <section class="model-panel">
    <p>Naledi completed the highly selective Brightpath Global Fellowship in the United States which is a specialized programmethat prepares fellows to found and lead high performing schools in underserved communities.Prior to establishing the Thabeni Academy, Naledi taught middle school humanities for seven years and worked as an education programme coordinator. Naledi holds an MS Degree in Education Policy from the University of Lakeshore-Riverton, where she was an Advanced Opportunity Fellow and a BAin education from Fairmont College.</p>
    <h2 class="section-title">Our Model</h2>
    <p style="margin-bottom:4px">Thabeni Academy has several unique features aimed to put all students on the path to university:</p>
    <ul class="feature-list">
      <li>University preparatory curriculum and learning environment</li>
      <li>Dual Language Programme (English and Zulu0</li>
      <li>Highly qualified, caring, and passionate educators and staff</li>
      <li>Creative Arts and movement classes</li>
      <li>Extended School Day</li>
      <li>Technology Integration across subject areas</li>
      <li style="grid-column:2">Extra-murals built into the school day</li>
    </ul>
  </section>

  <section class="core">
    <h2 class="section-title">Core Components</h2>
    <p class="core-intro">At Thabeni Academy, we have outlined four core components that will be prioritized, witheach area providing an avenue for achieving our mission of ensuring that all students are prepared with the academic and character skills that they need to be successful in university.</p>
    <div class="tiles">
      <div class="tile tile--justice">Social Justice Foundation
        <svg width="46" height="50" viewBox="0 0 46 50" aria-hidden="true" fill="none" stroke="#1a1a1a" stroke-width="3">
          <line x1="23" y1="4" x2="23" y2="44"/><line x1="6" y1="10" x2="40" y2="10"/><line x1="12" y1="46" x2="34" y2="46"/>
          <path d="M6 10 L1 26 H11 Z M40 10 L35 26 H45 Z"/>
        </svg>
      </div>
      <div class="tile tile--planning">Standards Based Unit and Lesson Planning
        <svg width="40" height="40" viewBox="0 0 40 40" aria-hidden="true"><path d="M6 34 L9 24 L28 5 L35 12 L16 31 Z" fill="#1a1a1a"/></svg>
      </div>
      <div class="tile tile--literacy">Literacy Focus
        <svg width="54" height="42" viewBox="0 0 54 42" aria-hidden="true" fill="none" stroke="#1a1a1a" stroke-width="4">
          <path d="M27 8 C20 3 10 3 3 6 V38 C10 35 20 35 27 40 C34 35 44 35 51 38 V6 C44 3 34 3 27 8 Z M27 8 V40"/>
        </svg>
      </div>
      <div class="tile tile--data">Data Driven Instruction
        <svg width="46" height="42" viewBox="0 0 46 42" aria-hidden="true" fill="#1a1a1a">
          <rect x="2" y="38" width="42" height="3"/><rect x="2" y="4" width="3" height="36"/>
          <rect x="10" y="26" width="5" height="12"/><rect x="18" y="20" width="5" height="18"/><rect x="26" y="23" width="5" height="15"/><rect x="34" y="12" width="5" height="26"/>
          <polyline points="10,20 20,12 28,16 40,4" fill="none" stroke="#1a1a1a" stroke-width="2"/>
        </svg>
      </div>
    </div>
  </section>

  <section class="questions">
    <h2 class="section-title">Questions</h2>
    <p>If you have questions, please contact a member of our team at <strong>+27 71-555-0148</strong> or by email at <strong>info@sizwefoundation.org.</strong></p>
  </section>
</main>
</body>
</html>
```